Business Card Design for Mabel's Larder

We make food for dogs.
Business Card Design (using the logo designed by you). Our Brand color is a bright canary yellow. For example our signage is predominantly yellow, with the logo in black. I'd like the card also to use that imagery.
Feel free to use the two sides creatively.
Vertical Design is also great.

Industry/Entity Type

Pet food

Contact Information for Business Card

Name, email, website, phone no

Font styles to use
Sans Serif

Colors
59FF00
82FF00
B8FF75
E3FFCB
F4FFEA
FFF300
FFF600
FEFA6F
FFFEC7
FFFEE8

Requirements
Nice to have
• A graphic in the same brush stroke style of the logo shoeing a doggy bowl of food

```html
<!DOCTYPE html>
<html lang="en">
<head>
<meta charset="utf-8">
<title>Mabel's Larder – Business Card</title>
<link rel="stylesheet" href="https://fonts.googleapis.com/css2?family=Oswald:wght@500&family=Open+Sans:wght@400;700&display=swap">
<style>
  :root {
    --backdrop: #2a2a2a;
    --card-yellow: #fde457;
    --ink: #111111;
    --card-radius: 26px;
  }
  * { box-sizing: border-box; margin: 0; padding: 0; }
  html, body {
    width: 1200px; height: 1108px; overflow: hidden;
    background: var(--backdrop);
  }
  .stage {
    position: relative; width: 1200px; height: 1108px;
    display: flex; justify-content: center; align-items: center; gap: 60px;
  }
  .card {
    position: relative;
    width: 380px; height: 640px;
    background: var(--card-yellow);
    border-radius: var(--card-radius);
    color: var(--ink);
  }
  .wordmark {
    font-family: 'Oswald', 'Arial Narrow', sans-serif;
    font-weight: 500;
    text-transform: uppercase;
    letter-spacing: 0.5px;
    line-height: 1;
    white-space: nowrap;
  }
  .card-front .wordmark {
    position: absolute; left: 0; right: 0; top: 370px;
    text-align: center; font-size: 44px;
  }
  .card-back { padding: 56px 40px 0 40px; }
  .person-name {
    font-family: 'Open Sans', sans-serif; font-weight: 700;
    font-size: 36px; line-height: 1.05; text-transform: uppercase;
  }
  .person-role {
    font-family: 'Open Sans', sans-serif; font-weight: 400;
    font-size: 22px; margin-bottom: 18px;
  }
  .contact-list { list-style: none; }
  .contact-item {
    display: flex; align-items: center; gap: 10px;
    font-family: 'Open Sans', sans-serif; font-size: 15px;
    margin-bottom: 9px;
  }
  .contact-icon {
    width: 22px; height: 22px; flex: none;
    background: var(--ink); border-radius: 3px;
    display: flex; align-items: center; justify-content: center;
  }
  .contact-icon svg { width: 14px; height: 14px; }
  .address {
    font-family: 'Open Sans', sans-serif; font-size: 17px;
    line-height: 1.35; margin-top: 8px;
  }
  .card-back .wordmark {
    position: absolute; left: 0; right: 0; bottom: 92px;
    text-align: center; font-size: 54px;
  }
</style>
</head>
<body>
<main class="stage">
  <section class="card card-front" aria-label="Card front">
    <p class="wordmark">Mabel's Larder</p>
  </section>

  <section class="card card-back" aria-label="Card back">
    <h1 class="person-name">Rosa Delgado</h1>
    <p class="person-role">Manager</p>
    <ul class="contact-list">
      <li class="contact-item">
        <span class="contact-icon">
          <svg viewBox="0 0 24 24"><path fill="#fde457" d="M6.6 10.8a15.1 15.1 0 0 0 6.6 6.6l2.2-2.2c.3-.3.7-.4 1-.2 1.1.4 2.3.6 3.6.6.6 0 1 .4 1 1V20c0 .6-.4 1-1 1A17 17 0 0 1 3 4c0-.6.4-1 1-1h3.5c.6 0 1 .4 1 1 0 1.3.2 2.5.6 3.6.1.3 0 .7-.2 1z"/></svg>
        </span>
        214-555-0187
      </li>
      <li class="contact-item">
        <span class="contact-icon">
          <svg viewBox="0 0 24 24"><rect x="3" y="6" width="18" height="12" fill="none" stroke="#fde457" stroke-width="2"/><path d="M3 6l9 7 9-7" fill="none" stroke="#fde457" stroke-width="2"/></svg>
        </span>
        hello@mabelslarder.com
      </li>
      <li class="contact-item">
        <span class="contact-icon">
          <svg viewBox="0 0 24 24" fill="none" stroke="#fde457" stroke-width="2"><circle cx="12" cy="12" r="9"/><ellipse cx="12" cy="12" rx="4" ry="9"/><path d="M3 12h18"/></svg>
        </span>
        www.mabelslarder.com
      </li>
    </ul>
    <p class="address">4821 Elm Grove Ln. Suite 210<br>Dallas, TX 75201</p>
    <p class="wordmark">Mabel's Larder</p>
  </section>
</main>
</body>
</html>
```